Got the awesome logo, now need the awesome business card

Want to use my just purchased logo on the backside of my card and to secure another logo by the same designer (Marcus) for the front side.
Updates

Reason: I have uploaded the logos. VOLK5 should be on the front of the card with my contact information and Volk5tan should be on the back. Thank you.

The logos have been uploaded and I have extended the deadline by 5 days. The VOLK% logo should be on the front with my contact information and the volk5tan should be on the back.

Industry/Entity Type

Business

Requirements
Must have
• Existing logo(s), clean background on front of card

```html
<!DOCTYPE html>
<html lang="en">
<head>
<meta charset="utf-8">
<title>Volk5tan Business Card</title>
<link rel="stylesheet" href="https://fonts.googleapis.com/css2?family=Arimo:wght@400;700&display=swap">
<style>
  :root {
    --backdrop: #9a9a9a;
    --card-light: #ffffff;
    --card-mid: #a9bfe3;
    --card-deep: #5a8ccc;
    --card-deeper: #2f74c2;
    --brand-ink: #444444;
    --text-light: #ffffff;
    --shadow: rgba(0, 0, 0, 0.45);
  }
  * { margin: 0; padding: 0; box-sizing: border-box; }
  html, body {
    width: 1200px; height: 1000px; overflow: hidden;
    background: var(--backdrop);
    font-family: "Arimo", Arial, sans-serif;
  }
  .stage { position: relative; width: 1200px; height: 1000px; }
  .card {
    position: absolute;
    width: 737px; height: 420px;
    box-shadow: 4px 6px 10px var(--shadow);
  }
  .card--back {
    left: 53px; top: 57px;
    background: linear-gradient(90deg, var(--card-light) 0%, var(--card-mid) 45%, var(--card-deep) 100%);
  }
  .card--front {
    left: 402px; top: 520px;
    background: linear-gradient(90deg, var(--card-light) 0%, #c9d6ee 35%, var(--card-deep) 75%, var(--card-deeper) 100%);
  }
  .wordmark {
    position: absolute;
    color: var(--brand-ink);
    font-weight: 400;
    line-height: 1;
    white-space: nowrap;
  }
  .tagline {
    position: absolute;
    color: var(--brand-ink);
    font-weight: 400;
    line-height: 1;
    white-space: nowrap;
  }
  .card--back .wordmark { left: 82px; top: 160px; font-size: 130px; }
  .card--back .tagline { left: 82px; top: 294px; font-size: 53px; }
  .card--front .wordmark { left: 23px; top: 60px; font-size: 70px; }
  .card--front .tagline { left: 24px; top: 137px; font-size: 34px; }
  .holder {
    position: absolute; right: 58px; top: 44px;
    color: var(--text-light); text-align: right; line-height: 1;
  }
  .holder__name { font-size: 44px; }
  .holder__role { font-size: 40px; margin-top: 2px; }
  .contacts {
    position: absolute; left: 300px; top: 270px;
    list-style: none; color: var(--text-light);
  }
  .contacts li {
    display: flex; align-items: center; gap: 8px;
    height: 31px; font-size: 21px; white-space: nowrap;
  }
  .contacts li.contacts__web { font-size: 18px; }
  .contacts svg { width: 34px; height: 26px; flex: none; }
</style>
</head>
<body>
<main class="stage">

  <section class="card card--back" aria-label="Card back">
    <p class="wordmark">Volk5tan</p>
    <p class="tagline">Executive Management</p>
  </section>

  <section class="card card--front" aria-label="Card front">
    <p class="wordmark">volk5</p>
    <p class="tagline">Management</p>

    <div class="holder">
      <p class="holder__name">Elena Hartwell</p>
      <p class="holder__role">Principal</p>
    </div>

    <ul class="contacts">
      <li>
        <svg viewBox="0 0 34 26" aria-hidden="true">
          <path d="M3 9 Q17 0 31 9 L28 13 L23 11 L23 8 Q17 6 11 8 L11 11 L6 13 Z" fill="#fff" opacity=".85"/>
          <rect x="6" y="13" width="22" height="11" rx="2" fill="#fff" opacity=".85"/>
          <circle cx="17" cy="18.5" r="3.2" fill="#7fa3d6"/>
        </svg>
        <span>555.014.2287</span>
      </li>
      <li>
        <svg viewBox="0 0 34 26" aria-hidden="true">
          <path d="M5 3 H29 Q31 3 31 5 V17 Q31 19 29 19 H13 L7 24 V19 H5 Q3 19 3 17 V5 Q3 3 5 3 Z" fill="none" stroke="#fff" stroke-width="2"/>
          <path d="M9 9 H25 M9 13 H21" stroke="#fff" stroke-width="2"/>
        </svg>
        <span>@volk5management</span>
      </li>
      <li>
        <svg viewBox="0 0 34 26" aria-hidden="true">
          <rect x="3" y="4" width="28" height="18" fill="none" stroke="#fff" stroke-width="2"/>
          <path d="M3 4 L17 15 L31 4 M3 22 L13 12 M31 22 L21 12" fill="none" stroke="#fff" stroke-width="2"/>
        </svg>
        <span>volk5management@mailbox.com</span>
      </li>
      <li class="contacts__web">
        <svg viewBox="0 0 34 26" aria-hidden="true">
          <g fill="none" stroke="#fff" stroke-width="1.8">
            <circle cx="16" cy="13" r="11"/>
            <ellipse cx="16" cy="13" rx="5" ry="11"/>
            <path d="M5 13 H27 M7 7 H25 M7 19 H25"/>
          </g>
        </svg>
        <span>www.profilehub.net/ElenaHartwellExecMgmt</span>
      </li>
    </ul>
  </section>

</main>
</body>
</html>
```